Business Card Design

We need a new business card design for our company, Lumen Forge.

Our website: www.brightrow7.ca

We are open to all ideas, from professional to very creative.
Updates

Design update requests:

1. We would like to see some examples with "BrightRow7" instead of "Lumen Forge" as the company name.
2. Would like to see "Software | Web | Branding" included on the card somewhere as well.

Thanks.

We are really trying to express the nature of our business through our business card.  "Lumen" can be misconstrued for the health industry, so use of "BrightRow7" and the "Software | Web | Branding" slogan are key to understanding our business.

We have uploaded a new PSD which includes a monitor, tablet, and phone screen.  This represents the flexibility of web applications and is another tool we would like to see used on business cards.

We will be eliminating designs today and will await updated designs with these new specs.

Thank-you.

Industry/Entity Type

Business

Requirements
Must have
• Content:
First M. Last
Managing Partner
e. email@brightrow7.ca
p. 555.555.5555

```html
<!DOCTYPE html>
<html lang="en">
<head>
<meta charset="utf-8">
<title>BrightRow7 – Business Card</title>
<link rel="stylesheet" href="https://fonts.googleapis.com/css2?family=Jost:wght@300;400&family=Open+Sans:wght@400&display=swap">
<style>
  :root {
    --orange: #f26522;
    --red: #ee3124;
    --ink: #1a1a1a;
    --grey: #8a8a8a;
    --rule: #c8c8c8;
    --paper: #ffffff;
    --tint: rgba(242, 101, 34, 0.14);
  }
  html, body {
    margin: 0;
    padding: 0;
    width: 1200px;
    height: 1000px;
    overflow: hidden;
    background: var(--paper);
  }
  .board {
    position: relative;
    width: 1200px;
    height: 1000px;
    font-family: "Jost", sans-serif;
  }
  .brand-gradient {
    background: linear-gradient(90deg, var(--orange), var(--red));
  }

  /* Title tab */
  .title-tab {
    position: absolute;
    left: 0; top: 98px;
    width: 286px; height: 60px;
    color: #fff;
    font-family: "Open Sans", sans-serif;
    font-size: 12.5px;
    line-height: 60px;
    text-indent: 38px;
  }

  /* Front card */
  .card-front {
    position: absolute;
    left: 432px; top: 67px;
    width: 737px; height: 420px;
    box-shadow: 1px 2px 5px rgba(0,0,0,0.35);
    overflow: hidden;
    color: #fff;
  }
  .card-front .hairline {
    position: absolute;
    height: 1px;
    background: rgba(255,255,255,0.3);
  }
  .hairline.top { left: 63px; top: 6px; width: 305px; }
  .hairline.bottom { left: 368px; top: 412px; width: 310px; }
  .pattern-glow {
    position: absolute;
    background: radial-gradient(ellipse at center, rgba(255,255,255,0.14), rgba(255,255,255,0) 70%);
  }
  .front-logo {
    position: absolute;
    left: 188px; top: 166px;
    display: flex;
    align-items: center;
    gap: 22px;
  }
  .logo-mark {
    background: rgba(255,255,255,0.55);
  }
  .front-logo .logo-mark { width: 52px; height: 52px; }
  .front-logo .logo-name {
    font-weight: 300;
    font-size: 52px;
    letter-spacing: 0.5px;
    line-height: 1;
  }
  .front-slogan {
    position: absolute;
    right: 148px; top: 232px;
    font-weight: 300;
    font-size: 17px;
    letter-spacing: 1.2px;
    white-space: nowrap;
  }
  .devices {
    position: absolute;
    border-radius: 4px;
    background: linear-gradient(135deg, #1f1f1f, #3a3a3a);
  }
  .card-front .devices {
    left: 202px; top: 341px;
    width: 104px; height: 64px;
  }
  .front-url {
    position: absolute;
    left: 324px; top: 372px;
    font-weight: 300;
    font-size: 14.5px;
    letter-spacing: 0.8px;
  }

  /* Back card */
  .card-back {
    position: absolute;
    left: 43px; top: 501px;
    width: 736px; height: 420px;
    background: var(--paper);
    box-shadow: 1px 2px 5px rgba(0,0,0,0.35);
    overflow: hidden;
  }
  .card-back .band {
    position: absolute;
    left: 48px; top: 0;
    width: 270px; height: 420px;
    color: #fff;
  }
  .band .pattern-glow { left: 60px; top: 95px; width: 160px; height: 210px; }
  .band-logo {
    position: absolute;
    left: 30px; top: 182px;
    display: flex;
    align-items: center;
    gap: 14px;
  }
  .band-logo .logo-mark { width: 30px; height: 30px; }
  .band-logo .logo-name {
    font-weight: 300;
    font-size: 26px;
    line-height: 1;
  }
  .band-url {
    position: absolute;
    right: 28px; top: 213px;
    font-weight: 300;
    font-size: 11px;
    letter-spacing: 0.5px;
  }
  .contact {
    position: absolute;
    right: 28px; top: 55px;
    text-align: right;
  }
  .contact .name {
    color: var(--orange);
    font-size: 16px;
    letter-spacing: 1.2px;
    margin: 0;
    line-height: 20px;
  }
  .contact .role {
    font-family: "Open Sans", sans-serif;
    color: var(--ink);
    font-size: 11px;
    margin: 4px 0 0;
  }
  .contact-rule {
    position: absolute;
    left: 345px; top: 106px;
    width: 363px; height: 1px;
    background: var(--rule);
  }
  .contact-lines {
    position: absolute;
    right: 30px; top: 113px;
    text-align: right;
    font-family: "Open Sans", sans-serif;
    font-size: 11px;
    color: #444;
    line-height: 25px;
  }
  .contact-lines .key { color: var(--orange); }
  .accent-bar {
    position: absolute;
    left: 730px; top: 57px;
    width: 4px; height: 98px;
    background: var(--orange);
  }
  .back-pattern {
    position: absolute;
    left: 442px; top: 180px;
    width: 200px; height: 235px;
    background: radial-gradient(ellipse at center, var(--tint), rgba(242,101,34,0) 72%);
  }
  .card-back .devices {
    left: 484px; top: 272px;
    width: 210px; height: 128px;
  }

  /* Footer caption */
  .caption {
    position: absolute;
    right: 110px; top: 947px;
    font-family: "Open Sans", sans-serif;
    font-size: 10.5px;
    color: var(--grey);
  }
  .caption .sep { margin: 0 9px; }
  .caption .site { color: var(--ink); }
  .caption .site b { color: var(--orange); font-weight: 400; }
</style>
</head>
<body>
<main class="board">

  <div class="title-tab brand-gradient">Brightrow7.ca lumen forge</div>

  <section class="card-front brand-gradient" aria-label="Business card front">
    <div class="hairline top"></div>
    <div class="hairline bottom"></div>
    <div class="pattern-glow" role="img" aria-label="Scattered translucent squares, top left" style="left:0;top:0;width:70px;height:170px;"></div>
    <div class="pattern-glow" role="img" aria-label="Scattered translucent squares around the logo" style="left:270px;top:110px;width:170px;height:200px;"></div>
    <div class="pattern-glow" role="img" aria-label="Scattered translucent squares, bottom right" style="left:670px;top:250px;width:67px;height:170px;"></div>

    <div class="front-logo">
      <span class="logo-mark"></span>
      <span class="logo-name">BRIGHTROW7</span>
    </div>
    <div class="front-slogan">Software | Web | Branding</div>

    <div class="devices" role="img" aria-label="Monitor, tablet and phone icon"></div>
    <div class="front-url">BRIGHTROW7.CA</div>
  </section>

  <section class="card-back" aria-label="Business card back">
    <div class="band brand-gradient">
      <div class="pattern-glow" role="img" aria-label="Scattered translucent squares"></div>
      <div class="band-logo">
        <span class="logo-mark"></span>
        <span class="logo-name">BRIGHTROW7</span>
      </div>
      <div class="band-url">BRIGHTROW7.CA</div>
    </div>

    <div class="contact">
      <p class="name">FIRST M. LAST</p>
      <p class="role">Managing Partner</p>
    </div>
    <div class="contact-rule"></div>
    <div class="contact-lines">
      <div><span class="key">E</span> - email@brightrow7.ca</div>
      <div><span class="key">P</span> - 555.555.5555</div>
    </div>
    <div class="accent-bar"></div>

    <div class="back-pattern" role="img" aria-label="Scattered pale orange squares"></div>
    <div class="devices" role="img" aria-label="Monitor, tablet and phone icon"></div>
  </section>

  <footer class="caption">
    Managing partner brightrow7 lumen forge<span class="sep">|</span><span class="site">www.<b>brightrow7</b>.ca</span>
  </footer>

</main>
</body>
</html>
```